Zielgruppe
Wir sind ein Business Center und vermieten Büro- und Konferenzräume. Wir richten uns an Unternehmen unterschiedlichster Branchen: Freelancer ohne eigenes Büro oder auch große Unternehmen, welche keine eigene freien Vakanzen haben, z. B. für Vorstellungsgespräche.
Aufgabenstellung
Flyer Din Lang, quer, gebunden an der kurzen Seite. 8 Seiten, inkl. Vorder- und Rückseite. Bitte kein Wickelfalz oder ähnliches, sondern eine Broschüre, gebunden mit Klammerheftung!!!
Frisches helles Design, ohne Schnörkel. Bilder mit etwas Text, dazu eine Seite über uns. Rückseite Kontaktdaten. Je eine Doppelseite für Konferenzraumvermietung und eine Doppelseite für Büroraum auf Zeit, eine Doppelseite für unsere weitere Leistungen, Telefonservice (Anrufannahme im namen unserer Kunden).
Unsere Räume sind sehr repräsentativ und modern eingerichtet mit hellen Designermöbeln. Das soll auch in der Broschüre klar werden.

```html
<!DOCTYPE html>
<html lang="de">
<head>
<meta charset="utf-8">
<title>NORVELL Broschüre</title>
<link href="https://fonts.googleapis.com/css2?family=Arimo:wght@400;500;700&display=swap" rel="stylesheet">
<style>
:root{
  --green:#c8dc52;
  --ink:#3a3a3a;
  --text:#444;
  --canvas:#efefef;
  --paper:#ffffff;
  --rule:#d9d9d9;
}
*{box-sizing:border-box;margin:0;padding:0}
html,body{width:840px;height:1200px;overflow:hidden;background:var(--canvas);font-family:'Arimo',Arial,sans-serif;color:var(--text)}
.canvas{position:relative;width:840px;height:1200px}
.page{position:absolute;width:397px;height:198px;background:var(--paper);box-shadow:0 1px 3px rgba(0,0,0,.12);overflow:hidden}
.page.inner-right{background:linear-gradient(90deg,#e6e6e6 0,#fafafa 18%,#fff 40%)}
.abs{position:absolute}
.photo{position:absolute}
.brand{position:absolute;font-weight:700;color:var(--ink);letter-spacing:.5px;white-space:nowrap}
.title{font-size:14px;font-weight:500;line-height:1.17;color:var(--ink)}
.title .hl{color:var(--green)}
.body{font-size:6.4px;line-height:1.25;color:var(--text)}
.checks{list-style:none;font-size:5px;line-height:1.2;color:#333}
.checks li{position:relative;padding-left:13px;margin-bottom:4.4px}
.checks li::before{content:"";position:absolute;left:2px;top:-1px;width:3px;height:6px;border:solid var(--green);border-width:0 1.6px 1.6px 0;transform:rotate(45deg)}
.bracket{position:absolute}
/* cover */
.cover{left:195.5px;top:38.7px;background:var(--green)}
.cover .sheet{position:absolute;inset:12px;background:var(--paper)}
.cover .welcome{position:absolute;left:17px;top:110px;font-size:13.5px;font-weight:500;line-height:1.25;color:var(--ink)}
/* price table */
.prices{position:absolute;left:29px;top:64px;width:166px;font-size:6.3px;border-collapse:collapse;color:#333}
.prices td{padding:2.2px 0 1.6px;border-bottom:1px solid var(--rule);vertical-align:top}
.prices td.num{text-align:right}
.prices tr.head td{border:0;font-size:5px;padding:0 0 1px}
.prices tr.opt td{font-weight:500;font-size:7px;padding-top:6px}
.side{position:absolute;right:0;top:0;width:109px;height:198px;background:var(--green)}
.side ul{list-style:none;position:absolute;left:11px;top:74px;font-size:6.4px;line-height:1.15;color:var(--ink)}
.side li{position:relative;padding-left:13px;margin-bottom:4.5px}
.side li::before{content:"→";position:absolute;left:0;top:-.5px;color:#fff}
/* back */
.back{left:233.6px;top:958px;background:var(--green);color:#fff}
.service{position:absolute;width:110px}
.service svg{position:absolute;left:0;top:0}
.service h3{margin-left:21px;font-size:6.4px;font-weight:700;color:var(--ink)}
.service p{margin:6px 0 0 21px;font-size:6.2px;line-height:1.25;color:#fff}
.contact{position:absolute;left:216px;top:136px;list-style:none;font-size:6.4px;color:var(--ink)}
.contact li{display:flex;align-items:center;gap:8px;margin-bottom:5.2px}
</style>
</head>
<body>
<div class="canvas">

  <!-- Cover -->
  <section class="page cover">
    <div class="sheet">
      <div class="brand" style="left:25px;top:32px;font-size:20px">NORVELL</div>
      <div class="photo" role="img" aria-label="Laptop und Tasse Kaffee auf weißem Schreibtisch, von oben fotografiert" style="left:148px;top:17px;width:208px;height:137px;background:radial-gradient(ellipse at 65% 50%,#cfcfd1 0,#ececec 45%,#fff 72%)"></div>
      <p class="welcome">WILLKOMMEN<br>IN IHREM<br>NEUEN <span style="color:var(--green)">NORVELL!</span></p>
    </div>
  </section>

  <!-- Konferenzraum: left -->
  <section class="page" style="left:23px;top:267px">
    <div class="photo" role="img" aria-label="Empfangsbereich mit hellem Holztresen" style="left:9.4px;top:9.4px;width:98px;height:52px;background:linear-gradient(160deg,#f1ede6,#c9a673)"></div>
    <div class="photo" role="img" aria-label="Konferenztisch mit Bildschirm an der Wand" style="left:9.4px;top:70px;width:98px;height:119px;background:linear-gradient(180deg,#ecebe8 0,#dedcd8 55%,#8a6447 100%)"></div>
    <div class="photo" role="img" aria-label="Heller Konferenzraum mit langem weißem Tisch, Stühlen und Fensterfront" style="left:115.5px;top:9.4px;width:272px;height:180px;background:linear-gradient(180deg,#efeeeb 0,#dfe2e4 35%,#bfbfbd 62%,#c59a6c 100%)"></div>
  </section>

  <!-- Konferenzraum: right -->
  <section class="page inner-right" style="left:420px;top:267px">
    <svg class="bracket" style="left:28px;top:18px" width="80" height="162" viewBox="0 0 80 162">
      <polyline points="79,13 79,1 1,1 1,161 79,161 79,54" fill="none" stroke="#c8dc52" stroke-width="1.6"/>
    </svg>
    <h2 class="title abs" style="left:40px;top:35px;white-space:nowrap"><span class="hl">KONFERENZRAUM ANMIETEN</span><br>IN DÜSSELDORF</h2>
    <p class="body abs" style="left:120px;top:82px;width:162px">Nutzen Sie unsere modernen Konferenz- und Tagungsräume für Meetings, Präsentationen, Gespräche, oder Schulungen. Unsere hellen, stylischen Räume werden auch Sie faszinieren. Präsentieren Sie sich vor Ihren Geschäftspartnern an einem tollen Ort. Unser Team erfüllt all Ihre Wünsche - vom leckeren Cappuccino bishin zu raffinierten Canapes.</p>
    <ul class="checks abs" style="left:291px;top:31px;width:90px">
      <li>bis zu 10 Teilnehmer</li>
      <li>bekannte Location im Kaiserhof</li>
      <li>persönlicher Empfang &amp; Betreuung</li>
      <li>55 Zoll 4k Fernseher</li>
      <li>Streaming-Box</li>
      <li>Screen-Sharing</li>
      <li>Konferenztelefon</li>
      <li>großes Whiteboard</li>
      <li>Flipchart</li>
      <li>Tiefgarage</li>
    </ul>
  </section>

  <!-- Büroanmietung: left -->
  <section class="page" style="left:23px;top:495.5px">
    <div class="photo" role="img" aria-label="Pflanze und Hängeleuchten vor Glaswand mit Stadtsilhouette" style="left:10.5px;top:9px;width:95px;height:179px;background:linear-gradient(180deg,#dcdcd8 0,#c9cbb8 50%,#c89a5e 100%)"></div>
    <div class="abs" style="left:115px;top:19px;width:166px;height:46px;border:1.6px solid var(--green)"></div>
    <h2 class="title abs" style="left:134px;top:36px;background:var(--paper);padding-right:6px"><span class="hl">BÜROANMIETUNG</span><br>IN DÜSSELDORF</h2>
    <p class="body abs" style="left:115px;top:96px;width:166px">Nach Vertragsunterzeichnung können Sie sofort einziehen: kein Umbau, keine Renovierung und wenn Sie wünschen, können Sie das Mietverhältnis kurzfristig wieder kündigen. Soviel Flexibiltät erhalten Sie nur bei uns!</p>
    <ul class="checks abs" style="left:290px;top:32px;width:90px">
      <li>Zugang 24/7</li>
      <li>persönlicher Empfang</li>
      <li>ab 15qm</li>
      <li>eigenes Firmenschild</li>
      <li>wöchentliche Reinigung inklusive</li>
      <li>kostenfreier Hochgeschwind-igkeits-Internetzugang</li>
      <li>große Schreibtische</li>
      <li>auf Wunsch inkl. Anrufan-nahme durch unser geschul-tes Personal</li>
      <li>optionale Anmietung eines Konferenzraumes mit bis zu 10 Plätzen</li>
      <li>Mitbenutzung der sanitären Einrichtungen und der Küche</li>
    </ul>
  </section>

  <!-- Büroanmietung: right -->
  <section class="page" style="left:420px;top:495.5px">
    <div class="photo" role="img" aria-label="Weißer Schreibtisch mit Laptop, Stehlampe und Bürostuhl" style="left:8px;top:10px;width:272px;height:182px;background:linear-gradient(180deg,#d9d6cf 0,#cfcbc3 62%,#ececea 100%)"></div>
    <div class="photo" role="img" aria-label="Bürogebäude an einer Straße mit Straßenbahn" style="left:289px;top:10px;width:100px;height:54px;background:linear-gradient(180deg,#e8ecef 0,#a9afb3 60%,#8e8a7c 100%)"></div>
    <div class="photo" role="img" aria-label="Lounge mit schwarzen Sesseln" style="left:289px;top:72px;width:100px;height:58px;background:linear-gradient(180deg,#eeeeea 0,#c9c7c1 55%,#3b3b3b 100%)"></div>
    <div class="photo" role="img" aria-label="Kaffeemaschine mit Cappuccino-Tasse" style="left:289px;top:138px;width:100px;height:54px;background:linear-gradient(90deg,#2a2624 0,#5a4a40 40%,#e9e3da 70%,#2e2c2b 100%)"></div>
  </section>

  <!-- Telefonservice: left -->
  <section class="page" style="left:23px;top:726px">
    <div class="abs" style="left:28px;top:19px;width:166px;height:46px;border:1.6px solid var(--green)"></div>
    <h2 class="title abs" style="left:47px;top:36px;background:var(--paper);padding-right:6px"><span class="hl">TELEFONSERVICE</span><br>CLEARCALL</h2>
    <div class="abs" style="left:288px;top:19px;width:80px;height:80px;background:var(--green);color:#fff;font-size:6.8px;line-height:1.3;padding:16px 12px">Mit ClearCall haben Sie einen entscheidenden Vorteil: <b>Erreichbarkeit!</b></div>
    <p class="body abs" style="left:28px;top:83px;width:255px">Ihre Anrufer werden begeistert sein, dass Sie ab sofort durchgängig erreichbar sind. Verzichten Sie zukünftig auf einen unpersönlichen Anrufbeantworter oder die Rufum-leitung auf Ihr Mobilfunktelefon.</p>
    <ul class="checks abs" style="left:28px;top:118px;width:170px">
      <li>Annahmezeiten: Mo.-Fr. 08:00 - 20:00 Uhr (individuell anpassbar)</li>
      <li>pauschale Abrechnung mit 1,00 Euro pro Anruf</li>
      <li>Anrufannahme mit Ihrem Firmennamen</li>
      <li>Abfrage von Name, Anrufgrund (in Form eines Stichwortes), Rufnummer, ggf. Emailadresse</li>
      <li>auf Wunsch Vermittlung an den gewünschten Ansprechpartner</li>
    </ul>
    <ul class="checks abs" style="left:202px;top:118px;width:160px">
      <li>deutsch- und englischsprachige Mitarbeiter</li>
      <li>ISDN Technologie - KEIN VOIP</li>
      <li>individuelle Einstellmöglichkeiten auf My NORVELL</li>
      <li>inkl. Anrufbeantworter</li>
      <li>Firmensitz: Düsseldorf</li>
      <li>mtl. kündbar</li>
    </ul>
  </section>

  <!-- Preise: right -->
  <section class="page inner-right" style="left:420px;top:726px">
    <h2 class="title abs" style="left:29px;top:37px;white-space:nowrap"><span class="hl">PREISE</span> - TARIF CLEARCALL<sup style="font-size:8px">1</sup></h2>
    <table class="prices">
      <tr class="head"><td></td><td></td><td class="num">Euro</td></tr>
      <tr><td>Grundgebühr</td><td>pro Monat</td><td class="num">29,95</td></tr>
      <tr><td>Anrufannahme</td><td>pro Anruf</td><td class="num">1,00</td></tr>
      <tr><td>Benachrichtigung</td><td>pro Mail</td><td class="num"></td></tr>
      <tr class="opt"><td colspan="3">optional, sofern Sie dies wünschen</td></tr>
      <tr><td>Weiterleiten in Ihr dt.<br>Festnetz</td><td>pro Minute</td><td class="num">0,04</td></tr>
      <tr><td>Weiterleiten in Ihr dt.<br>Mobilnetz</td><td>pro Minute</td><td class="num">0,20</td></tr>
      <tr><td>SMS Benachrichtigung</td><td>pro SMS</td><td class="num">0,12</td></tr>
    </table>
    <p class="abs" style="left:201px;top:160px;width:78px;font-size:4.7px;line-height:1.2;color:#333">1) Vertragslaufzeit auf unbestim-mte Zeit, 7 Werktage vor Monatsende kündbar</p>
    <aside class="side">
      <div class="brand" style="left:15px;top:29px;font-size:12px">NORVELL</div>
      <ul>
        <li>Leistungen<br>Telefonservice</li>
        <li>Bürovermietung</li>
        <li>Telefonsekretariat</li>
        <li>Telefonannahme</li>
        <li>Virtual Office</li>
        <li>Telefonzentrale</li>
        <li>Büroservice</li>
        <li>Call Center</li>
      </ul>
    </aside>
  </section>

  <!-- Back cover -->
  <section class="page back">
    <div class="service" style="left:28px;top:27px">
      <svg width="12" height="12" viewBox="0 0 12 12"><path d="M2 1l2 0 1 3-1.5 1a6 6 0 0 0 3.5 3.5L8 7l3 1v2c0 .6-.4 1-1 1A9 9 0 0 1 1 2c0-.6.4-1 1-1z" fill="#fff"/></svg>
      <h3>Telefonservice</h3>
      <p>ClearCall Sekretariatsservice, schon ab 1,00 Euro/Anruf</p>
    </div>
    <div class="service" style="left:143px;top:27px;width:115px">
      <svg width="13" height="13" viewBox="0 0 13 13"><circle cx="4" cy="4" r="3" fill="none" stroke="#fff" stroke-width="1.5"/><path d="M6 6l6 6M9 9l2-1M10.5 10.5l1.5-1" stroke="#fff" stroke-width="1.5"/></svg>
      <h3>Exklusive Büroanmietung</h3>
      <p>hochwertig, provisionsfrei und repräsentativ in bester Lage</p>
    </div>
    <div class="service" style="left:260px;top:27px">
      <svg width="13" height="13" viewBox="0 0 13 13"><rect x="1" y="3" width="3" height="9" fill="#fff"/><rect x="5" y="1" width="7" height="11" fill="none" stroke="#fff" stroke-width="1.2"/><path d="M7 5h3M7 7h3M7 9h3" stroke="#fff"/></svg>
      <h3>ClearNumbers</h3>
      <p>Ihre neue Düsseldorfer Ruf- und Faxnummer</p>
    </div>
    <div class="service" style="left:28px;top:72px">
      <svg width="13" height="12" viewBox="0 0 13 12"><rect x="1" y="3" width="11" height="8" rx="1" fill="#fff"/><rect x="4.5" y="1" width="4" height="2.5" fill="none" stroke="#fff"/></svg>
      <h3>Virtual Office</h3>
      <p>Zeigen Sie Präsenz in der Landeshauptstadt Düsseldorf</p>
    </div>
    <div class="service" style="left:143px;top:72px;width:115px">
      <svg width="13" height="13" viewBox="0 0 13 13"><rect x="1" y="3" width="9" height="9" rx="1" fill="none" stroke="#fff" stroke-width="1.3"/><path d="M5 8l6-6 1.5 1.5-6 6H5z" fill="#fff"/></svg>
      <h3>Hotline</h3>
      <p>First-Level-Support, Bestellan-nahme u.v.m.</p>
    </div>
    <div class="service" style="left:260px;top:72px;width:120px">
      <svg width="14" height="12" viewBox="0 0 14 12"><circle cx="7" cy="3" r="2.3" fill="#fff"/><circle cx="2.8" cy="4" r="1.7" fill="#fff"/><circle cx="11.2" cy="4" r="1.7" fill="#fff"/><path d="M3 11a4 4 0 0 1 8 0zM0 10a3 3 0 0 1 3.5-3M14 10a3 3 0 0 0-3.5-3" fill="#fff"/></svg>
      <h3>Termine</h3>
      <p>Wir arbeiten u. a. mit Termalo, Kalendo und Praxilo</p>
    </div>
    <div class="brand" style="left:35px;top:147px;font-size:18px">NORVELL</div>
    <ul class="contact">
      <li><svg width="6" height="7" viewBox="0 0 6 7"><path d="M3 7L.6 3.6A2.6 2.6 0 1 1 5.4 3.6z" fill="#fff"/></svg>Lindenhofstraße 120, 40210 Düsseldorf</li>
      <li><svg width="6" height="6" viewBox="0 0 6 6"><circle cx="3" cy="3" r="3" fill="#fff"/><path d="M3 1.2V3h1.4" stroke="#c8dc52" stroke-width=".8" fill="none"/></svg>Mo.-Fr. 08:00 - 20:00</li>
      <li><svg width="6" height="6" viewBox="0 0 12 12"><path d="M2 1l2 0 1 3-1.5 1a6 6 0 0 0 3.5 3.5L8 7l3 1v2c0 .6-.4 1-1 1A9 9 0 0 1 1 2c0-.6.4-1 1-1z" fill="#fff"/></svg>0800 - 4 270 318</li>
      <li><svg width="6" height="5" viewBox="0 0 6 5"><rect width="6" height="5" fill="#fff"/><path d="M0 0l3 2.5L6 0" stroke="#c8dc52" stroke-width=".6" fill="none"/></svg>info@norvell-office.de</li>
    </ul>
  </section>

</div>
</body>
</html>
```